Signage Design Project

We need a logo and signage for the shopfront of a personal fitness training gym and coaching facility. We want the signage to cover the glass shopfront windows which consist of 4 glass windows with dimensions: 1 of 200cm x 180cm, 2 of 180cm x 135cm and 1 of 180cm x 180cm. The windows that are 200x 180 and 180x180 are the most visable/ important. We want the 200x180 to display the logo and our name which is "Harbourline Fitness Centre" with further information of: Your personal training studio and boutique coaching gym Ph: 9472 3815.
For the window with 180 x 180cm measurement we want to list the services we provide which are:
Personal Training Sessions | Group Classes|Weight Loss |Toning & Sculpting|Bodybuilding I Cardio|Weights| Kettlebells| Boxing| Circuits I Team Building Programs| Boot Camp I Healthy Lifestyle & Wellness Coaching
The 2 windows 180x135cm are diagonal to the entry of the shop. We want them to be the same and plainer in design with the words: Harbourline Fitness Centre
Personal Training Studio and Boutique Coaching Gym
The signage design also includes an acrylic window box that lights up which is to display the logo and Harbourline Fitness Centre

```html
<!DOCTYPE html>
<html lang="en">
<head>
<meta charset="utf-8">
<title>Harbourline Fitness Centre – Shopfront Sign</title>
<link href="https://fonts.googleapis.com/css2?family=Questrial&display=swap" rel="stylesheet">
<style>
  :root {
    --page: #ffffff;
    --lime: #a8b526;
    --blue-light: #00b6ec;
    --blue-mid: #0090bb;
    --blue-deep: #006d8c;
    --ink: #f4f6f7;
  }
  * { margin: 0; padding: 0; box-sizing: border-box; }
  html, body {
    width: 1200px;
    height: 900px;
    overflow: hidden;
    background: var(--page);
  }
  .canvas {
    position: relative;
    width: 1200px;
    height: 900px;
    font-family: "Questrial", "Century Gothic", sans-serif;
    color: var(--ink);
  }
  .sign-backdrop {
    position: absolute;
    left: 0;
    top: 0;
  }
  .brand-dot {
    position: absolute;
    left: 554px;
    top: 118px;
    width: 76px;
    height: 76px;
    border-radius: 50%;
    background: var(--ink);
  }
  .brand-name {
    position: absolute;
    left: 163px;
    width: 884px;
    top: 232px;
    text-align: center;
    font-size: 100px;
    line-height: 1.2;
    letter-spacing: 2px;
    text-transform: uppercase;
  }
  .brand-frame {
    position: absolute;
    left: 315px;
    top: 392px;
    width: 582px;
    height: 98px;
    border: 4px dashed var(--ink);
    border-radius: 30px;
    display: flex;
    align-items: center;
    justify-content: center;
  }
  .brand-sub {
    font-size: 60px;
    line-height: 1;
    letter-spacing: 1px;
  }
  .tagline {
    position: absolute;
    left: 163px;
    width: 910px;
    top: 536px;
    text-align: center;
    font-size: 40px;
    line-height: 44px;
    letter-spacing: 5px;
  }
  .contact {
    position: absolute;
    left: 357px;
    top: 714px;
    display: flex;
    align-items: center;
    gap: 22px;
  }
  .contact-number {
    font-size: 66px;
    line-height: 1;
    letter-spacing: 4px;
  }
</style>
</head>
<body>
  <main class="canvas">
    <svg class="sign-backdrop" width="1200" height="900" viewBox="0 0 1200 900" aria-hidden="true">
      <defs>
        <radialGradient id="panelGlow" cx="620" cy="40" r="820" gradientUnits="userSpaceOnUse">
          <stop offset="0" stop-color="var(--blue-light)"/>
          <stop offset="0.5" stop-color="var(--blue-mid)"/>
          <stop offset="1" stop-color="var(--blue-deep)"/>
        </radialGradient>
      </defs>
      <rect class="corner-band" x="163" y="53" width="884" height="794" fill="var(--lime)"/>
      <path class="panel" fill="url(#panelGlow)"
            d="M163,372 C205,200 330,70 512,53 L1047,53 L1047,530 C1005,705 880,830 700,847 L163,847 Z"/>
    </svg>

    <span class="brand-dot" aria-hidden="true"></span>
    <h1 class="brand-name">Harbourline</h1>
    <div class="brand-frame"><span class="brand-sub">Fitness Centre</span></div>

    <p class="tagline">Your personal training<br>studio &amp; boutique<br>coaching gym</p>

    <div class="contact">
      <svg class="phone-icon" width="36" height="58" viewBox="0 0 36 58" aria-label="Phone">
        <rect x="11" y="0" width="5" height="8" rx="2" fill="var(--ink)"/>
        <rect x="0" y="6" width="36" height="52" rx="8" fill="var(--ink)"/>
        <rect x="6" y="13" width="24" height="18" rx="3" fill="var(--blue-deep)"/>
        <circle cx="18" cy="44" r="4" fill="var(--blue-deep)"/>
      </svg>
      <span class="contact-number">9472-3815</span>
    </div>
  </main>
</body>
</html>
```